Accountancy practice needs a wordpress website redesign for growth

We are a growing accountancy practice - headcount and revenues have doubled in the last 2 years. We are continuing to grow. We only had a website made around 12 months ago but the company we used offered very little in terms of creativity and ideas of how to make it look modern and eye-catching. We want to redesign the website to make it look premium and professional because we are starting to launch more marketing and drive more traffic to the site.

The current website is www.tolvardaccountants.co.uk. The website was built in wordpress.

The logo has been uploaded. The main 2 colour hex codes are: 0E74BC and 14A79D.

We are open to changing the fonts in the website and welcome suggestions for this too.

Following on from this we will launch a project to design brochures and one-page flyers that we can fill with useful information about what we do and also create lead-generators to download from the website. So the design of the website will influence the overall brand and feel of all of the marketing collateral.

Target Market(s)

Property businesses and entrepreneurial, growth mindset clients

Industry/Entity Type

Accountancy

Number of Pages Required

3 page

Font styles to use
Sans Serif

Colors

Designer to choose colors to be used in the design.

Requirements
Must have
• A modern and professional feel. 3 fonts - most websites seem to use 3 different fonts now and I like this. We have our green and blue colours but I do not want too much of this all over the site, stick to blacks, whites and greys with the blue and green used for emphasis and accents.
Nice to have
• The coloured spaces should have some "depth" to them, eg a small pattern in the white spaces so its not just a solid whie background.

```html
<!DOCTYPE html>
<html lang="en">
<head>
<meta charset="utf-8">
<title>Tolvard Accountants</title>
<link rel="stylesheet" href="https://fonts.googleapis.com/css2?family=Cinzel:wght@500;700&family=Montserrat:wght@400;500;600;700;800&family=Open+Sans:wght@400;600&display=swap">
<style>
:root{
  --blue:#0E74BC;
  --teal:#14A79D;
  --navy:#0b3b66;
  --ink:#1d1d1f;
  --grey:#5b6470;
  --mist:#e9f5f4;
  --white:#ffffff;
}
*{box-sizing:border-box;margin:0;padding:0}
html,body{width:1200px;height:5008px;overflow:hidden}
body{font-family:"Open Sans",Arial,sans-serif;color:var(--ink);background:var(--white);position:relative}
section,header,footer{position:absolute;left:0;width:1200px}
.btn{display:inline-block;font-family:"Montserrat",sans-serif;font-weight:600;font-size:13px;letter-spacing:.5px;text-transform:uppercase;color:var(--white);background:var(--blue);padding:12px 22px;text-decoration:none}
.eyebrow{font-family:"Montserrat",sans-serif;font-size:12px;font-weight:600;letter-spacing:2px;text-transform:uppercase;color:var(--teal)}
.serif-title{font-family:"Cinzel",serif;font-weight:700;color:var(--blue);letter-spacing:1px}
.centered{text-align:center}
.rule{width:60px;height:3px;background:var(--teal);margin:10px auto 0}
.ph{position:absolute}

/* header */
.site-header{top:0;height:72px;background:var(--white);z-index:3;display:flex;align-items:center;justify-content:space-between;padding:0 48px}
.brand{display:flex;align-items:center;gap:10px;font-family:"Montserrat",sans-serif;font-weight:800;font-size:20px;color:var(--blue);line-height:1;letter-spacing:1px}
.brand .mark{width:22px;height:22px;background:var(--teal)}
.nav{display:flex;align-items:center;gap:24px;font-family:"Montserrat",sans-serif;font-size:13px;font-weight:600;color:var(--blue)}
.nav a{color:var(--blue);text-decoration:none;text-transform:uppercase}
.nav a.active{border-bottom:2px solid var(--blue);padding-bottom:3px}

/* hero */
.hero{top:72px;height:548px;background:linear-gradient(100deg,#1b2430 0%,#3a4a5a 45%,#8a9098 100%)}
.hero-text{position:absolute;left:190px;top:170px;color:var(--white)}
.hero-text h1{font-family:"Montserrat",sans-serif;font-weight:800;font-size:46px;line-height:1.12;text-transform:uppercase;letter-spacing:.5px}
.hero-text .btn{margin-top:40px}

/* about */
.about{top:620px;height:580px;background:var(--white)}
.about-copy{position:absolute;left:200px;top:210px;width:400px}
.about-copy h2{font-size:28px;margin-top:4px}
.about-copy p{font-size:13px;line-height:1.6;color:var(--grey);margin-top:16px}
.about-copy .lead{color:var(--ink);font-weight:600;margin-top:14px}
.about-copy .btn{margin-top:20px;font-size:11px;padding:10px 18px}
.about .blob{left:720px;top:130px;width:420px;height:330px;border-radius:50% 45% 50% 40%;background:linear-gradient(135deg,#cde9e7,#14A79D 70%,#0E74BC)}
.about .photo{left:760px;top:150px;width:330px;height:310px;border-radius:50%;background:linear-gradient(160deg,#c7a58e,#7d5c4c 60%,#2f2a2a)}

/* who */
.who{top:1200px;height:400px;border-top:1px solid #eee}
.who-head{position:absolute;top:80px;width:100%}
.who-head h2{font-size:32px}
.cards{position:absolute;top:200px;left:110px;display:flex;gap:32px}
.card{width:220px;height:180px;text-align:center;padding-top:20px}
.card svg{width:60px;height:60px}
.card h3{font-family:"Montserrat",sans-serif;font-weight:700;font-size:15px;color:var(--teal);text-transform:uppercase;margin-top:8px;line-height:1.2}
.card p{font-size:12px;line-height:1.5;color:var(--grey);margin-top:8px;padding:0 14px}
.card.active{background:var(--teal);color:var(--white)}
.card.active h3{color:var(--white)}
.card.active .more{display:inline-block;margin-top:10px;font-family:"Montserrat",sans-serif;font-size:10px;font-weight:700;background:var(--white);color:var(--teal);padding:5px 12px}

/* booking band */
.booking{top:1640px;height:240px;background:linear-gradient(90deg,#0a5f9c,#0E74BC 60%,#2b88c8)}
.booking-copy{position:absolute;left:200px;top:78px;color:var(--white);font-family:"Montserrat",sans-serif}
.booking-copy .small{font-size:22px;font-weight:600}
.booking-copy .big{font-size:38px;font-weight:800;margin-top:2px}
.booking .btn{position:absolute;left:752px;top:102px;background:var(--white);color:var(--blue);text-transform:none;font-size:15px;padding:12px 26px}

/* why */
.why{top:1920px;height:1290px;background:linear-gradient(180deg,#dff1f0 0%,#f4fbfa 40%,#ffffff 100%)}
.why-head{position:absolute;top:90px;width:100%}
.why-head h2{font-size:32px}
.why-intro{position:absolute;left:160px;top:250px;width:430px}
.why-intro .lead{font-family:"Montserrat",sans-serif;font-size:19px;font-weight:500;line-height:1.35;color:var(--ink)}
.why-intro p{font-size:13px;line-height:1.6;color:var(--grey);margin-top:16px}
.why .blob1{left:620px;top:220px;width:440px;height:340px;border-radius:48% 52% 45% 55%;background:linear-gradient(135deg,#14A79D,#0E74BC)}
.why .photo1{left:650px;top:240px;width:380px;height:300px;border-radius:50%;background:linear-gradient(140deg,#e8e2d8,#8d7a66 60%,#3b3430)}
.why .blob2{left:130px;top:620px;width:420px;height:330px;border-radius:52% 48% 55% 45%;background:linear-gradient(135deg,#0E74BC,#14A79D)}
.why .photo2{left:160px;top:640px;width:360px;height:290px;border-radius:50%;background:linear-gradient(160deg,#d9dde2,#6f7780 55%,#2a2e33)}
.why-list{position:absolute;left:590px;top:660px;width:470px}
.why-list h3{font-family:"Montserrat",sans-serif;font-size:19px;font-weight:500}
.why-list ul{list-style:none;margin-top:16px}
.why-list li{font-size:13px;line-height:1.55;color:var(--grey);padding-left:18px;position:relative;margin-bottom:14px}
.why-list li::before{content:"";position:absolute;left:0;top:7px;width:6px;height:6px;background:var(--teal);border-radius:50%}
.why-list p{font-size:13px;line-height:1.6;color:var(--ink);margin-top:10px}
.why .btn{position:absolute;left:470px;top:1200px;text-transform:none;font-size:14px}

/* software */
.software{top:3240px;height:580px;background:var(--white)}
.soft-head{position:absolute;top:60px;width:100%}
.soft-head h2{font-size:30px}
.soft-intro{position:absolute;left:190px;top:180px;width:820px;text-align:center;font-size:13px;line-height:1.6;color:var(--grey)}
.partners{position:absolute;left:90px;top:380px;width:1020px;display:flex;align-items:center;justify-content:space-between}
.arrow{width:30px;height:30px;border-radius:50%;border:1px solid #ccc;display:flex;align-items:center;justify-content:center;color:var(--grey);font-size:14px}
.partner{width:210px;height:80px;border:1px solid #dde3e8;display:flex;align-items:center;justify-content:center;gap:10px;font-family:"Montserrat",sans-serif;font-weight:700;font-size:20px;color:var(--grey)}
.partner .dot{width:22px;height:22px;border-radius:50%;background:var(--teal)}

/* insights */
.insights{top:3820px;height:690px;background:var(--white)}
.ins-head{position:absolute;top:50px;width:100%}
.ins-head h2{font-size:30px}
.posts{position:absolute;left:260px;top:240px;display:flex;gap:80px}
.post{width:300px}
.post .thumb{height:170px;background:linear-gradient(135deg,#d5d9de,#6b7178)}
.post .thumb2{background:linear-gradient(135deg,#e9e9ea,#3b3f45)}
.post h3{font-family:"Montserrat",sans-serif;font-weight:700;font-size:15px;color:var(--teal);text-transform:uppercase;line-height:1.3;margin-top:16px}
.post p{font-size:12px;line-height:1.55;color:var(--grey);margin-top:10px}
.post .read{display:block;margin-top:12px;font-family:"Montserrat",sans-serif;font-weight:700;font-size:11px;color:var(--blue)}
.ins-arrow{position:absolute;top:400px;width:34px;height:34px;border-radius:50%;background:var(--teal);color:var(--white);display:flex;align-items:center;justify-content:center;font-size:14px}
.insights .btn{position:absolute;left:428px;top:600px}

/* footer */
.site-footer{top:4510px;height:498px;background:var(--teal);color:var(--white)}
.foot-brand{position:absolute;top:50px;width:100%;display:flex;justify-content:center;align-items:center;gap:14px;font-family:"Montserrat",sans-serif;font-weight:800;font-size:40px;letter-spacing:2px}
.foot-brand .mark{width:40px;height:40px;background:var(--white)}
.foot-cols{position:absolute;top:180px;left:80px;display:flex;gap:80px}
.foot-cols h4{font-family:"Montserrat",sans-serif;font-size:14px;font-weight:700;margin-bottom:12px}
.foot-cols li{list-style:none;font-size:12px;line-height:1.8}
.foot-cols .col{width:190px}
.foot-cols .col.contact{width:260px}
.company{position:absolute;top:380px;width:100%;text-align:center;font-size:13px;line-height:1.6}
.badges{position:absolute;right:60px;top:380px;display:flex;gap:14px}
.badge{width:70px;height:46px;background:var(--white);border-radius:4px}
.legal{position:absolute;bottom:0;height:46px;width:100%;background:var(--navy);display:flex;justify-content:center;align-items:center;gap:18px;font-family:"Montserrat",sans-serif;font-size:11px;font-weight:600;letter-spacing:.5px}
</style>
</head>
<body>

<header class="site-header">
  <div class="brand"><span class="mark"></span>TOLVARD ACCOUNTANTS</div>
  <nav class="nav">
    <a class="active" href="#">About us</a>
    <a href="#">Who we help</a>
    <a href="#">Thoughts</a>
    <a href="#">Switching accountants</a>
    <a class="btn" href="#">Book a discovery call</a>
  </nav>
</header>

<section class="hero">
  <div class="ph" role="img" aria-label="Person working on a laptop with a calculator and papers at a desk" style="inset:0;background:linear-gradient(100deg,rgba(20,28,38,.85),rgba(20,28,38,.3))"></div>
  <div class="hero-text">
    <h1>Your accounts<br>will be done.<br>What else can<br>we do for you?</h1>
    <a class="btn" href="#">Book a discovery call</a>
  </div>
</section>

<section class="about">
  <div class="about-copy">
    <div class="eyebrow">About us</div>
    <h2 class="serif-title">Tolvard Accountants</h2>
    <p>We understand that running and growing your business takes an incredible amount of effort. You don't want to be bogged down worrying about getting paperwork done on time. You want to know that the decisions you make are based on sound, correct advice and you want to be able to talk to someone you trust for that advice. So don't worry – we will make sure your accounts and taxes are done.</p>
    <p class="lead">Let's see what else we can do for you.</p>
    <a class="btn" href="#">Get in touch</a>
  </div>
  <div class="ph blob"></div>
  <div class="ph photo" role="img" aria-label="Smiling team member at a desk in the office"></div>
</section>

<section class="who">
  <div class="who-head centered">
    <div class="eyebrow">Our service</div>
    <h2 class="serif-title">Who we help?</h2>
    <div class="rule"></div>
  </div>
  <div class="cards">
    <div class="card">
      <svg viewBox="0 0 60 60"><rect x="8" y="14" width="20" height="40" fill="#0E74BC"/><rect x="32" y="24" width="20" height="30" fill="#14A79D"/><g fill="#fff"><rect x="12" y="20" width="4" height="4"/><rect x="20" y="20" width="4" height="4"/><rect x="12" y="30" width="4" height="4"/><rect x="20" y="30" width="4" height="4"/><rect x="36" y="30" width="4" height="4"/><rect x="44" y="30" width="4" height="4"/></g></svg>
      <h3>Property investors and developers</h3>
      <p>Busy with your investments and need to ensure your accounts are in order?</p>
    </div>
    <div class="card">
      <svg viewBox="0 0 60 60"><rect x="10" y="10" width="40" height="30" fill="none" stroke="#0E74BC" stroke-width="3"/><circle cx="22" cy="48" r="5" fill="#14A79D"/><circle cx="38" cy="48" r="5" fill="#0E74BC"/></svg>
      <h3>Consultants</h3>
      <p>When you partner with us it allows you to focus on your area of expertise while we take</p>
    </div>
    <div class="card active">
      <svg viewBox="0 0 60 60"><path d="M18 10v18a12 12 0 0 0 24 0V10" fill="none" stroke="#fff" stroke-width="3"/><path d="M30 40v6a8 8 0 0 0 16 0v-6" fill="none" stroke="#fff" stroke-width="3"/><circle cx="46" cy="36" r="4" fill="#fff"/></svg>
      <h3>Medical professionals</h3>
      <span class="more">Find out more</span>
    </div>
    <div class="card">
      <svg viewBox="0 0 60 60"><rect x="8" y="22" width="20" height="18" rx="3" fill="#0E74BC"/><rect x="32" y="22" width="20" height="18" rx="3" fill="#14A79D"/><rect x="22" y="27" width="16" height="8" fill="#0E74BC"/></svg>
      <h3>Buying or selling a business</h3>
      <p>When buying or selling a business you need to know</p>
    </div>
  </div>
</section>

<section class="booking">
  <div class="booking-copy">
    <div class="small">Set A Date Today To Speak To Our Team</div>
    <div class="big">Book An Appointment</div>
  </div>
  <a class="btn" href="#">Book An Appointment</a>
</section>

<section class="why">
  <div class="why-head centered">
    <div class="eyebrow">Our work</div>
    <h2 class="serif-title">Why choose us?</h2>
    <div class="rule"></div>
  </div>
  <div class="why-intro">
    <div class="lead">At Tolvard Accountants, we know you are the kind of people who want to be successful and have the time to do the things you love doing and to see the people you love seeing.</div>
    <p>To do that, you need to focus on the important issues in your business and know that the numbers and filing deadlines are taken care of. You also need to know that you are getting reliable feedback and advice that can be used to make decisions.</p>
    <p>The problem is (and we hear it from a lot of people) that the current accountant only does numbers and nothing else, or they don't reply to you, or they don't offer any solutions. Whatever the problem is, the end result is you are micromanaging and not getting the results you want.</p>
  </div>
  <div class="ph blob1"></div>
  <div class="ph photo1" role="img" aria-label="Hands working on paperwork with a calculator"></div>
  <div class="ph blob2"></div>
  <div class="ph photo2" role="img" aria-label="Professional working at a laptop in a bright office"></div>
  <div class="why-list">
    <h3>Relax, we've got this covered.</h3>
    <ul>
      <li>We're here at the end of the phone to talk you through those decisions – you'll have a dedicated point of contact (you can even give them your number so they can call you).</li>
      <li>We'll make sure your deadlines aren't missed.</li>
      <li>We'll tell you if we think we aren't doing things in the best way possible.</li>
      <li>We'll even attend your board meetings, if you'd like, to get into the business and provide that detailed input you are looking for.</li>
    </ul>
    <p>If that sounds like the relationship you want, then book a video call with us. Then you can start doing the things you love doing and seeing the people you love seeing.</p>
  </div>
  <a class="btn" href="#">Book An Appointment</a>
</section>

<section class="software">
  <div class="soft-head centered">
    <div class="eyebrow">Technologies</div>
    <h2 class="serif-title">Software solutions</h2>
    <div class="rule"></div>
  </div>
  <p class="soft-intro">We are proud to work with a range of software solutions to ensure your accountancy procedures are running as smoothly as possible. Software can make a significant difference to your business and through the use of these solutions we can save you time and money, whilst also improving your business efficiency.</p>
  <div class="partners">
    <div class="arrow">&#8249;</div>
    <div class="partner"><span class="dot"></span>Ledgerbook</div>
    <div class="partner">Sumwise</div>
    <div class="partner"><span class="dot"></span>Taxfold</div>
    <div class="partner">Meetlane</div>
    <div class="arrow">&#8250;</div>
  </div>
</section>

<section class="insights">
  <div class="ins-head centered">
    <div class="eyebrow">Thoughts</div>
    <h2 class="serif-title">Latest insights and thoughts</h2>
    <div class="rule"></div>
  </div>
  <div class="ins-arrow" style="left:170px">&#8249;</div>
  <div class="posts">
    <article class="post">
      <div class="thumb" role="img" aria-label="Professionals reviewing documents at a meeting"></div>
      <h3>Spring statement – property market update – what does it mean for the property prices?</h3>
      <p>Raging inflation, Covid, Brexit, war in Europe, and tax receipts rising. How can this be and what does it mean for you as a business owner or property investor?</p>
      <span class="read">READ MORE &rsaquo;</span>
    </article>
    <article class="post">
      <div class="thumb thumb2" role="img" aria-label="Business person in a suit signing papers"></div>
      <h3>4 benefits property investors missed in the Chancellor's spring statement</h3>
      <p>Raging inflation, Covid, Brexit, war in Europe, and tax receipts rising. How can this be and what does it mean for you as a business owner or property investor?</p>
      <span class="read">READ MORE &rsaquo;</span>
    </article>
  </div>
  <div class="ins-arrow" style="left:996px">&#8250;</div>
  <a class="btn" href="#">Check out our other free advice</a>
</section>

<footer class="site-footer">
  <div class="foot-brand"><span class="mark"></span>TOLVARD ACCOUNTANTS</div>
  <div class="foot-cols">
    <div class="col contact">
      <h4>Contact Us</h4>
      <ul><li>01632 960 481</li><li>info@tolvardaccountants.co.uk</li><li>12 Mill Lane, Ashbridge, AB1 2CD</li></ul>
    </div>
    <div class="col">
      <h4>About Us</h4>
      <ul><li>Meet The Team</li><li>Our Values</li><li>Software Solutions</li><li>Vacancies</li></ul>
    </div>
    <div class="col">
      <h4>Services</h4>
      <ul><li>Company Services</li><li>Personal Services</li><li>Advisory Services</li></ul>
    </div>
    <div class="col">
      <h4>Who We Help</h4>
      <ul><li>Property Investors and Developers</li><li>Consultants</li><li>Medical Professionals</li><li>Buying or Selling a Business</li></ul>
    </div>
  </div>
  <div class="company">Company No.: 10482265<br>Registered office address: 12 Mill Lane, Ashbridge, AB1 2CD</div>
  <div class="badges"><div class="badge"></div><div class="badge"></div></div>
  <div class="legal"><span>PRIVACY POLICY</span>|<span>COOKIES POLICY</span>|<span>TERMS OF BUSINESS</span></div>
</footer>

</body>
</html>
```